Locksmith Store 474747 Signage

Design Brief: Locksmith Store Signage – "Locksmith 474747" [ΚΛΕΙΔΑΡΑΣ 474747 (in Greek)]
We are looking for a spectacular and professional sign design for the exterior of our locksmith store.
Signage Dimensions:
• Width: 6 meters
• Height: 1.5 meters
• Shopfront window Width: 6 meters, Height: 2.5 meters
Key Requirements (in order of importance):
1. It must be immediately clear that this is a locksmith store. [ΚΛΕΙΔΑΡΑΣ (in Greek)]
2. The store name "474747", (which is also the phone number 5550474747), should be highly visible and visually striking because this is the number that customers are calling when they are locked out.
3. The signage should also clearly communicate that except for house keys, which is obvious for a locksmith store the services we provide are:
o All kinds of house keys. ΚΛΕΙΔΙΑ ΣΠΙΤΙΩΝ(in Greek) (There is no key that we cannot do)
o Immobiliser car keys = ΚΛΕΙΔΙΑ ΑΥΤΟΚΙΝΗΤΩΝ (in Greek)
We unlock every car that exist, we program new immobilizer keys – remote controls, even if all keys are lost, we repair or change broken cells of car keys, we change batteries.
o High-security locks = ΚΛΕΙΔΑΡΙΕΣ ΑΣΦΑΛΕΙΑΣ (in Greek) we sell the best high security locks in the planet
o Armoured doors = ΠΟΡΤΕΣ ΑΣΦΑΛΕΙΑΣ (in Greek) (this may not be so important to be on the signage.
Visual Style:
We are open to creative direction, but the design should be eye-catching, professional, and modern, something that will stand out on a busy street and instantly tell customers who we are and what we offer. Also, you may use the shopfront window for graphic designs. Also, we are open if a part of the signage is digital.
________________________________________
Updates
Hello Designers,
Thank you so much for your effort and the designs you've shared.
I realized I forgot to mention that you can refer to my website at www.474747-keys.example.gr for more context.
Additionally, I’ve just uploaded two new photos: one showing the store with a black outline at the dimensions of the signage, and another with the large double-bit key placed in a different position to demonstrate that it is moveable.
Thanks again for your dedication!
Target Market(s)
every person that has a key
Look and feel
Each slider illustrates characteristics of the customer's brand and the style your logo design should communicate.

```html
<!DOCTYPE html>
<html lang="el">
<head>
<meta charset="utf-8">
<title>ΚΛΕΙΔΑΡΑΣ 474747 – Πινακίδα καταστήματος</title>
<link rel="stylesheet" href="https://fonts.googleapis.com/css2?family=Fira+Sans+Extra+Condensed:wght@700;800&display=swap">
<style>
  :root {
    --page-bg: #1b1b1b;
    --steel-light: #e6e7e8;
    --steel-mid: #c9cacc;
    --steel-dark: #a9abad;
    --brand-red: #ee1c1c;
    --ink-black: #0a0a0a;
    --band-black: #070707;
    --outline-white: #ffffff;
  }
  html, body {
    margin: 0;
    width: 1200px;
    height: 1200px;
    overflow: hidden;
    background: var(--page-bg);
  }
  .signboard {
    position: absolute;
    left: 40px;
    top: 505px;
    width: 1120px;
    height: 189px;
    display: block;
  }
  .sign-text {
    font-family: "Fira Sans Extra Condensed", "Arial Narrow", sans-serif;
  }
  .trade-name {
    font-weight: 800;
    fill: var(--brand-red);
    stroke: var(--outline-white);
    stroke-width: 5;
    paint-order: stroke;
  }
  .area-code {
    font-weight: 800;
    fill: var(--brand-red);
    stroke: var(--outline-white);
    stroke-width: 4;
    paint-order: stroke;
  }
  .hotline-number {
    font-weight: 800;
    fill: var(--ink-black);
    stroke: var(--outline-white);
    stroke-width: 6;
    paint-order: stroke;
  }
  .service-line {
    font-weight: 700;
    fill: var(--brand-red);
    stroke: var(--outline-white);
    stroke-width: 3;
    paint-order: stroke;
  }
  .service-ring {
    fill: none;
    stroke: var(--brand-red);
    stroke-width: 7;
  }
</style>
</head>
<body>
<svg class="signboard" viewBox="0 0 1835 310" xmlns="http://www.w3.org/2000/svg" aria-label="ΚΛΕΙΔΑΡΑΣ 5550 474.747">
  <defs>
    <linearGradient id="brushedSteel" x1="0" y1="0" x2="1" y2="1">
      <stop offset="0" stop-color="var(--steel-mid)"/>
      <stop offset="0.35" stop-color="var(--steel-light)"/>
      <stop offset="0.7" stop-color="var(--steel-mid)"/>
      <stop offset="1" stop-color="var(--steel-dark)"/>
    </linearGradient>
    <filter id="dropShadow" x="-10%" y="-10%" width="120%" height="130%">
      <feDropShadow dx="4" dy="6" stdDeviation="4" flood-color="#000" flood-opacity="0.45"/>
    </filter>
    <radialGradient id="houseKeyTones" cx="0.4" cy="0.4" r="0.7">
      <stop offset="0" stop-color="#e8e4e0"/>
      <stop offset="1" stop-color="#8c8a88"/>
    </radialGradient>
    <radialGradient id="carKeyTones" cx="0.5" cy="0.5" r="0.7">
      <stop offset="0" stop-color="#d9b8a4"/>
      <stop offset="1" stop-color="#2b2b2b"/>
    </radialGradient>
    <linearGradient id="doorTones" x1="0" y1="0" x2="1" y2="0">
      <stop offset="0" stop-color="#4a4640"/>
      <stop offset="0.6" stop-color="#5e5850"/>
      <stop offset="1" stop-color="#2e2b28"/>
    </linearGradient>
    <linearGradient id="lockTones" x1="0" y1="0" x2="1" y2="0">
      <stop offset="0" stop-color="#5a4a3e"/>
      <stop offset="0.5" stop-color="#b9b9b9"/>
      <stop offset="1" stop-color="#4e4036"/>
    </linearGradient>
  </defs>

  <rect class="steel-panel" x="0" y="0" width="1835" height="310" fill="url(#brushedSteel)"/>

  <circle class="bullet-dot" cx="62" cy="47" r="20" fill="var(--ink-black)"/>
  <text class="sign-text area-code" transform="translate(82 283) rotate(-90)" font-size="92" textLength="190" lengthAdjust="spacingAndGlyphs" filter="url(#dropShadow)">5550</text>
  <text class="sign-text trade-name" x="167" y="87" font-size="86" textLength="425" lengthAdjust="spacingAndGlyphs" filter="url(#dropShadow)">ΚΛΕΙΔΑΡΑΣ</text>
  <text class="sign-text hotline-number" x="102" y="283" font-size="262" textLength="555" lengthAdjust="spacingAndGlyphs" filter="url(#dropShadow)">474.747</text>

  <g class="service-photo" role="img" aria-label="Φωτογραφία: χέρι κρατά κλειδί σπιτιού">
    <circle cx="857" cy="120" r="112" fill="url(#houseKeyTones)"/>
  </g>
  <circle class="service-ring" cx="857" cy="120" r="112"/>

  <g class="service-photo" role="img" aria-label="Φωτογραφία: κλειδί αυτοκινήτου με τηλεχειριστήριο στην παλάμη">
    <circle cx="1129" cy="120" r="112" fill="url(#carKeyTones)"/>
  </g>
  <circle class="service-ring" cx="1129" cy="120" r="112"/>

  <g class="service-photo" role="img" aria-label="Φωτογραφία: άκρη πόρτας ασφαλείας με πείρους">
    <circle cx="1400" cy="120" r="112" fill="url(#doorTones)"/>
  </g>
  <circle class="service-ring" cx="1400" cy="120" r="112"/>

  <g class="service-photo" role="img" aria-label="Φωτογραφία: κλειδαριά ασφαλείας με χερούλι">
    <circle cx="1672" cy="120" r="112" fill="url(#lockTones)"/>
  </g>
  <circle class="service-ring" cx="1672" cy="120" r="112"/>

  <polygon class="services-band" points="687,240 1835,240 1835,310 652,310" fill="var(--band-black)"/>
  <text class="sign-text service-line" x="702" y="292" font-size="44" textLength="1115" lengthAdjust="spacingAndGlyphs">ΚΛΕΙΔΙΑ ΣΠΙΤΙΩΝ • ΚΛΕΙΔΙΑ ΑΥΤΟΚΙΝΗΤΩΝ • ΚΛΕΙΔΑΡΙΕΣ ΑΣΦΑΛΕΙΑΣ</text>
</svg>
</body>
</html>
```